Book Cover

Book Title: THE QUIET LEDGER
Book Sub Title: Notes on slowing the daily rush and shaping a calmer household rhythm
Vibe: Professional, stylish, trustworthy (high-end men's fashion)
Website (for inspiration): www.brindlequarry.com
Attached: a potential photo to use for the cover, but open to other options (from our website)

```html
<!DOCTYPE html>
<html lang="en">
<head>
<meta charset="utf-8">
<title>The Quiet Ledger – Book Cover</title>
<link href="https://fonts.googleapis.com/css2?family=Oswald:wght@500;600&family=Roboto:wght@500&display=swap" rel="stylesheet">
<style>
  :root {
    --page-bg: #ececec;
    --cover-black: #0b0c10;
    --title-white: #ffffff;
    --title-red: #e3080d;
    --chair-red: #8e0d12;
    --shadow-blue: #0f1a28;
  }
  * { margin: 0; padding: 0; box-sizing: border-box; }
  html, body {
    width: 1200px;
    height: 1200px;
    overflow: hidden;
    background: var(--page-bg);
  }
  .canvas {
    position: relative;
    width: 1200px;
    height: 1200px;
  }
  .book-cover {
    position: absolute;
    left: 212px;
    top: 20px;
    width: 776px;
    height: 1160px;
    background: var(--cover-black);
    overflow: hidden;
    color: var(--title-white);
    text-align: center;
  }
  .cover-photo {
    position: absolute;
    left: 0;
    top: 500px;
    width: 100%;
    height: 660px;
    background:
      radial-gradient(ellipse 26% 22% at 52% 34%, rgba(20,22,30,0.95) 0%, rgba(20,22,30,0.6) 60%, rgba(20,22,30,0) 100%),
      radial-gradient(ellipse 34% 40% at 52% 40%, var(--chair-red) 0%, #4a070b 55%, rgba(11,12,16,0) 100%),
      linear-gradient(160deg, var(--shadow-blue) 0%, var(--cover-black) 45%, #111215 100%);
  }
  .cover-photo::after {
    content: "";
    position: absolute;
    inset: 0;
    background: linear-gradient(to bottom, var(--cover-black) 0%, rgba(11,12,16,0) 12%, rgba(11,12,16,0) 80%, rgba(11,12,16,0.85) 100%);
  }
  .title {
    position: absolute;
    left: 0;
    top: 36px;
    width: 100%;
    font-family: "Oswald", sans-serif;
    font-weight: 600;
    font-size: 165px;
    line-height: 167px;
    letter-spacing: 1px;
    white-space: nowrap;
  }
  .title-line { display: block; }
  .title-line--white { color: var(--title-white); }
  .title-line--red { color: var(--title-red); }
  .subtitle {
    position: absolute;
    left: 60px;
    right: 60px;
    top: 382px;
    font-family: "Roboto", sans-serif;
    font-weight: 500;
    font-size: 25px;
    line-height: 46px;
    text-transform: uppercase;
    letter-spacing: 0.3px;
  }
  .author {
    position: absolute;
    left: 0;
    width: 100%;
    bottom: 10px;
    font-family: "Oswald", sans-serif;
    font-weight: 500;
    font-size: 46px;
    letter-spacing: 12px;
  }
</style>
</head>
<body>
  <main class="canvas">
    <article class="book-cover">
      <div class="cover-photo" role="img" aria-label="Photograph of a man in a dark suit and red tie seated in a red leather wingback chair in a dim room"></div>
      <h1 class="title">
        <span class="title-line title-line--white">THE QUIET</span>
        <span class="title-line title-line--red">LEDGER</span>
      </h1>
      <p class="subtitle">Notes on slowing the daily rush and shaping a calmer household rhythm</p>
      <p class="author">AUTHOR NAME</p>
    </article>
  </main>
</body>
</html>
```